We are a printed circuit board manufacturer. Need a company professional web site to allow our potential customers to know more about our background, capability and our products. The web site will contain three languages, which are Chinese, English and Japanese. Our audience are mainly electronic companies that procure printed circuit boards. I have a word document that have all the required text in all three languages. The final design should communicate the impression that we embrace quality, trustworthiness and long term partnership business principles.
We should have sections that allow us to post pictures of our facilities.
I have added the three files in three different languages.
Some of the information is below:
Background
RVD Worldwide Limited (RVD) was set up in Hong Kong in 2007 by two Hong Kong entrepreneurs, Mr. Lok Fai Tam and Mr. Wai Ho. We acquired the single sided printed circuit board factory located in Dongguan City, Guangdong Province, China, from Valtor Corporation of the U.S. in 2007. In addition to RVD, Mr. Tam and Mr. Ho also own Brightrail Systems Company Limited, a semiconductor company based in Hong Kong since 1997 with a total investment of over US$100 million. Brightrail is engaged in the manufacturing of flexible substrates and MEMS assembly business.
RVD has been awarded TS 16949 and ISO14000 certificates since 2009 and 2004 respectively.
Business Principles
RVD Worldwide Limited strives to be a professional top notched printed circuit board supplier. We embrace four “EXCELLENCE” principles, namely, excellence in quality, excellence in prices, excellence in services and excellence in on time delivery.
We approach each customer with a long-term partnership view that delivers the lowest ownership costs and highest total values to our customers. We customize quotations and solutions in order to allow our customers to win more businesses. We believe by thinking from our customers’ points of view we will be able to create a WIN-WIN relationship.
Customers
Due to our excellent quality, services and production systems, RVD Worldwide Limited manage to service a number of large Japanese and US customers, which include:
Technical capability overview
Below is an overview of our current capability:
Target Market(s)
Electronic companies buyers
Industry/Entity Type
Business
Requirements
Must have
- Capability description
Should not have
- no cartoon

```html
<!DOCTYPE html>
<html lang="en">
<head>
<meta charset="utf-8">
<title>RVD Worldwide Limited</title>
<link href="https://fonts.googleapis.com/css2?family=Open+Sans:ital,wght@0,400;0,600;0,700;1,400&family=Tinos&display=swap" rel="stylesheet">
<style>
:root{
  --green:#3f8f1c;
  --green-dark:#2e6f12;
  --green-text:#1f8a2c;
  --navy:#06124a;
  --text:#333;
  --muted:#555;
  --link:#2a6fc9;
  --red:#d63a2a;
  --footer:#232323;
  --footer-bar:#1b1b1b;
  --panel:#ececec;
  --line:#d9d9d9;
}
*{box-sizing:border-box;margin:0;padding:0}
html,body{width:794px;height:1200px;overflow:hidden;background:#fff}
body{font-family:"Open Sans",Arial,sans-serif;color:var(--text)}
.page{position:relative;width:794px;height:1200px;overflow:hidden}
.abs{position:absolute}

/* header */
.header{left:0;top:0;width:794px;height:97px;background:linear-gradient(#fff,#d6d6d6)}
.logo{left:93px;top:18px;line-height:1}
.logo-mark{font-size:28px;font-weight:700;color:var(--green-dark);letter-spacing:2px}
.logo-sub{font-size:8px;font-weight:700;color:var(--green-dark);margin-top:2px}
.lang{left:622px;top:28px;width:78px;height:18px;border:1px solid #bbb;background:#fff;font-size:6.5px;padding:4px 5px;color:#444}
.lang b{font-weight:700}
.lang::after{content:"";position:absolute;right:5px;top:7px;border:3px solid transparent;border-top-color:#888}
.nav{left:93px;top:72px;width:607px;height:25px;background:linear-gradient(#5aa82a,var(--green-dark));border-radius:4px 4px 0 0;display:flex}
.nav a{color:#fff;text-decoration:none;font-size:11px;font-weight:600;display:flex;align-items:center;justify-content:center;border-right:1px solid rgba(255,255,255,.3);height:100%}

/* hero */
.hero{left:0;top:97px;width:794px;height:233px;background:var(--navy)}
.hero-panel{left:93px;top:97px;width:213px;height:233px;background:linear-gradient(135deg,#f2f2f4,#d4d6de);border-right:2px solid #e2561f}
.hero-title{left:107px;top:122px;font-family:Tinos,"Times New Roman",serif;font-size:19px;line-height:21px;color:#111}
.hero-title span{color:var(--red)}
.hero-text{left:109px;top:177px;width:190px;font-size:8.5px;line-height:14.5px;color:#222}
.btn{height:22px;width:103px;border-radius:11px;color:#fff;font-size:9.5px;display:flex;align-items:center;justify-content:center}
.btn-green{left:148px;top:248px;background:linear-gradient(#4fa52a,#2d7513)}
.btn-red{left:148px;top:282px;background:linear-gradient(#ef5a4a,#c42516)}
.hero-visual{left:308px;top:97px;width:486px;height:233px;background:radial-gradient(ellipse at 45% 55%,#1fa83a 0,#0e5a8c 30%,#1c66d6 55%,#0a1f86 85%)}

/* main column */
.h2{font-size:14.5px;font-weight:600;color:#222}
.h2 span{color:var(--green-text)}
.p{font-size:8px;line-height:15px;color:var(--text)}
.more{font-size:8px;font-style:italic;color:var(--red)}
.divider{height:1px;background:linear-gradient(90deg,transparent,#ccc,transparent)}
.service-img{left:93px;top:563px;width:76px;height:50px;border:2px solid #fff;box-shadow:0 0 0 1px #ccc;background:linear-gradient(135deg,#8aa0b8,#3e6b50)}
.products{left:93px;top:683px;width:412px;height:160px;background:var(--panel)}
.card{width:195px;height:88px;background:#fff;border:1px solid #ddd;padding:6px}
.card div{width:100%;height:100%}
.pcb1{background:linear-gradient(135deg,#3d6b2e,#1a2e18 60%,#6b7a3e)}
.pcb2{background:linear-gradient(135deg,#1f6b3a,#2f8f52 50%,#144a26)}
.prod-title{font-size:8.5px;color:var(--link)}
.clients{left:93px;top:882px;width:412px;height:80px;background:linear-gradient(#fff,#ececec);border:1px solid #e2e2e2}
.client{top:12px;width:64px;height:54px;background:#fff;border:1px solid #ccc;box-shadow:0 1px 2px rgba(0,0,0,.2);display:flex;align-items:center;justify-content:center;font-size:9px;font-weight:700;color:#222;gap:3px}
.client i{display:block;width:6px;height:6px;background:var(--red)}

/* sidebar */
.box{width:160px;background:#f3f3f3;border-bottom:2px solid #e8c889}
.box-head{height:26px;color:#fff;font-size:12px;font-weight:600;padding:4px 12px}
.head-green{background:linear-gradient(#5aa82a,var(--green-dark))}
.head-dark{background:linear-gradient(#666,#3c3c3c)}
.cap-list{list-style:none;padding:3px 12px 6px}
.cap-list li{font-size:8.5px;color:#333;height:22.3px;line-height:22px;border-bottom:1px solid #e2e2e2;padding-left:9px;position:relative}
.cap-list li::before{content:"›";position:absolute;left:0;color:#888}
.cap-list li:last-child{border-bottom:none}
.quote{font-size:8.5px;line-height:14px;font-style:italic;color:#555}
.blog-item{position:absolute;left:12px;width:140px}
.blog-item svg{position:absolute;left:0;top:2px}
.blog-item h4{font-size:8.5px;font-weight:600;color:#1d3f8f;padding-left:14px}
.blog-item p{font-size:7.5px;line-height:14px;color:#444;padding-left:14px}
.view-all{left:645px;top:935px;width:44px;height:16px;border-radius:3px;background:linear-gradient(#5aa82a,var(--green-dark));color:#fff;font-size:8px;font-weight:600;display:flex;align-items:center;justify-content:center}

/* footer */
.footer{left:0;top:982px;width:794px;height:183px;background:var(--footer)}
.f-h{font-size:14.5px;color:#fff}
.f-sub{font-size:8.5px;color:#5bb8e6}
.f-text{font-size:7.5px;line-height:13.5px;color:#ddd}
.f-text .big{font-size:12px;color:#6cc04a}
.social{font-size:8px;color:#fff;line-height:10px}
.social small{display:block;font-size:6.5px;color:#888}
.social i{position:absolute;left:-14px;top:1px;width:8px;height:8px;background:#6a8ac8}
.field{width:90px;height:17px;border:1px solid #444;background:#171717;font-size:6.5px;color:#999;padding:4px 5px}
.send{left:587px;top:1127px;width:44px;height:16px;border-radius:3px;background:linear-gradient(#5aa82a,var(--green-dark));color:#fff;font-size:8px;font-weight:700;display:flex;align-items:center;justify-content:center}
.bottom{left:0;top:1165px;width:794px;height:35px;background:var(--footer-bar);border-top:1px solid #333}
.copy{left:93px;top:1177px;font-size:8px;color:#ddd}
.bottom-nav{right:94px;top:1177px;font-size:8px;color:#ddd;display:flex;gap:14px}
</style>
</head>
<body>
<div class="page">

  <header>
    <div class="abs header"></div>
    <div class="abs logo">
      <div class="logo-mark">RVD</div>
      <div class="logo-sub">Worldwide Limited</div>
    </div>
    <div class="abs lang"><b>Language:</b> English</div>
    <nav class="abs nav">
      <a style="width:63px">Home</a>
      <a style="width:80px">About Us</a>
      <a style="width:81px">Products</a>
      <a style="width:77px">Services</a>
      <a style="width:136px">Technical Capability</a>
      <a style="width:103px">Infrastructure</a>
      <a style="width:67px;border:none">Clients</a>
    </nav>
  </header>

  <section class="hero-block">
    <div class="abs hero"></div>
    <div class="abs hero-panel"></div>
    <h1 class="abs hero-title"><span>Lorem Ipsum</span> is simple<br>dummy printing...</h1>
    <p class="abs hero-text">Lorem Ipsum is simply dummy typesetting the industry lorem ipsum&nbsp; text of the printing &amp; typesetting industry lorem ipsum has been the industry's for on standard.</p>
    <div class="abs btn btn-green">Click for Capability</div>
    <div class="abs btn btn-red">Click for Prducts</div>
    <div class="abs hero-visual" role="img" aria-label="Electronic circuitry over a glowing blue world map"></div>
  </section>

  <main>
    <h2 class="abs h2" style="left:93px;top:351px">Welcome to <span>RVD Worldwide Limited</span></h2>
    <p class="abs p" style="left:93px;top:375px;width:412px">Lorem Ipsum is simply dummy text of the printing and typesetting industry. Lorem Ipsum has been the industry's for on standard dummy text ever since the 1500s, when an unknown printer took a galley of type and scrambled it to make a passages, and more recently with desktop publishing.</p>
    <p class="abs p" style="left:93px;top:424px;width:412px">Lorem Ipsum is simply dummy text of the printing and typesetting industry. Lorem Ipsum has been the industry's&nbsp; into standard dummy text ever since the 1500s, when an unknown printer took a galley of type and scrambled it to make a type specimen book. It has survived not only five centuries, but also the leap into electronic typesetting, remaining go&nbsp; essentially unchanged. It was popularised in the 1960s with the release of Letraset sheets containing lorem Ipsum play&nbsp; type specimen book.</p>
    <div class="abs more" style="left:458px;top:505px">⊕ Read More</div>
    <div class="abs divider" style="left:93px;top:525px;width:412px"></div>

    <h2 class="abs h2" style="left:93px;top:538px">Our Services</h2>
    <div class="abs service-img" role="img" aria-label="Technician testing a circuit board"></div>
    <p class="abs p" style="left:180px;top:560px;width:325px">Lorem Ipsum is simply dummy text of the printing and typesetting industry. Lorem Ipsum has been the industry's for on standard dummy text ever since the 1500s, when an unknown printer took a galley of type and scrambled it to make a passages, and more recently with desktop publishing centuries.</p>
    <div class="abs more" style="left:458px;top:625px">⊕ Read More</div>

    <h2 class="abs h2" style="left:92px;top:657px">Products</h2>
    <div class="abs products"></div>
    <div class="abs card" style="left:99px;top:687px"><div class="pcb1" role="img" aria-label="Single layered printed circuit board with a chip"></div></div>
    <div class="abs card" style="left:305px;top:687px"><div class="pcb2" role="img" aria-label="Multi layered green printed circuit board"></div></div>
    <div class="abs prod-title" style="left:99px;top:792px">Singal layered printed circuit board</div>
    <div class="abs prod-title" style="left:302px;top:792px">Double &amp; Multi layered printed circuit board</div>
    <p class="abs p" style="left:99px;top:809px;width:195px">Lorem Ipsum is simply dummy text of the printing and typesetting industry standard dummy text.</p>
    <p class="abs p" style="left:302px;top:809px;width:195px">Lorem Ipsum is simply dummy text of the printing and typesetting industry standard dummy text.</p>

    <h2 class="abs h2" style="left:93px;top:856px">Our Client</h2>
    <div class="abs clients">
      <div class="abs client" style="left:12px"><i></i>Kestrel</div>
      <div class="abs client" style="left:91px">Norvane</div>
      <div class="abs client" style="left:170px">Altamor</div>
      <div class="abs client" style="left:253px">Quorin</div>
      <div class="abs client" style="left:334px">Helvik</div>
    </div>
  </main>

  <aside>
    <div class="abs box" style="left:541px;top:355px;height:190px">
      <div class="box-head head-green">Technical Capability</div>
      <ul class="cap-list">
        <li>Raw Materials</li>
        <li>Plating</li>
        <li>Printing Processes</li>
        <li>Punching And CNC Process</li>
        <li>Depth Tolerance</li>
        <li>Surface Finishing</li>
        <li>Specification for carbon</li>
      </ul>
    </div>

    <div class="abs box" style="left:541px;top:563px;height:168px">
      <div class="box-head head-dark">Testimonials</div>
      <p class="abs quote" style="left:13px;top:50px;width:136px">Lorem Ipsum is simply dummy text of the printing and typesetting into industry lorem ipsum has been the industry's for on standard...</p>
      <div class="abs" style="left:13px;top:134px;width:134px;height:1px;background:var(--line)"></div>
      <div class="abs" style="right:13px;top:145px;font-size:8.5px;color:var(--red)">Dana Holt</div>
    </div>

    <div class="abs box" style="left:541px;top:747px;height:216px;background:#e4e4e4">
      <div class="box-head head-dark">Latest Blog</div>
      <div class="blog-item" style="top:36px"><svg width="10" height="9" viewBox="0 0 10 9"><path d="M1 1h8v5H4L2 8V6H1z" fill="#fff" stroke="#888" stroke-width=".8"/></svg><h4>Neque porro est ipsum quia</h4><p>Lorem Ipsum is simply dummy text of the printing &amp; text.</p></div>
      <div class="blog-item" style="top:82px"><svg width="10" height="9" viewBox="0 0 10 9"><path d="M1 1h8v5H4L2 8V6H1z" fill="#fff" stroke="#888" stroke-width=".8"/></svg><h4>Neque porro est ipsum quia</h4><p>Lorem Ipsum is simply dummy text of the printing &amp; text.</p></div>
      <div class="blog-item" style="top:129px"><svg width="10" height="9" viewBox="0 0 10 9"><path d="M1 1h8v5H4L2 8V6H1z" fill="#fff" stroke="#888" stroke-width=".8"/></svg><h4>Neque porro est ipsum quia</h4><p>Lorem Ipsum is simply dummy text of the printing &amp; text.</p></div>
    </div>
    <div class="abs view-all">View All</div>
  </aside>

  <footer>
    <div class="abs footer"></div>
    <h3 class="abs f-h" style="left:93px;top:1004px">Contact</h3>
    <div class="abs f-sub" style="left:93px;top:1035px">Hong Kong Business Office</div>
    <div class="abs f-text" style="left:93px;top:1048px">RVD Worldwide Limited<br>28/F Harbour Point<br>17 Kelford Road<br>Email: sales@rvdboards.example<br>Phone: <span class="big">(852)30000481</span><br>Fax: <span class="big">(852)30000482</span></div>
    <div class="abs f-sub" style="left:243px;top:1035px">China Factory</div>
    <div class="abs f-text" style="left:243px;top:1048px">RVD Worldwide (Dongguan) Limited<br>8 Xinmao East 3 Road<br>52 Industrial District<br>Qingshan Town, Dongguan<br>Guangdong Province, China 523000<br>Phone: <span class="big">(86)769-80000571</span><br>Fax: <span class="big">(86)769-80000572</span></div>

    <h3 class="abs f-h" style="left:441px;top:1004px">Follow Us</h3>
    <div class="abs social" style="left:458px;top:1036px"><i></i>Linkwall<small>news, updates, previews</small></div>
    <div class="abs social" style="left:458px;top:1064px"><i></i>Chirpline<small>news, updates</small></div>
    <div class="abs social" style="left:458px;top:1092px"><i></i>Snapfold<small>previews,outtakes</small></div>

    <h3 class="abs f-h" style="left:587px;top:1004px">Request Quote</h3>
    <div class="abs field" style="left:587px;top:1036px">Name:</div>
    <div class="abs field" style="left:587px;top:1062px">Email:</div>
    <div class="abs field" style="left:587px;top:1088px;width:114px;height:28px">Massage:</div>
    <div class="abs send">SEND</div>

    <div class="abs bottom"></div>
    <div class="abs copy">© 2012 RVD Worldwide limited | All Rights Reserved</div>
    <nav class="abs bottom-nav"><span>Home</span><span>About Us</span><span>Products</span><span>Services</span><span>Technical Capability</span><span>Infrastructure</span></nav>
  </footer>

</div>
</body>
</html>
```